Criação de Kit Layout de Posts para Redes Sociais (Facebook, Instagram e etc) para Construção & Engenharia
A empresa queria:
" TRABALHAMOS COM LOCAÇÃO, VENDA DE EQUIPAMENTOS, MONTAGEM E PROJETOS DE ANDAIME E ESCORAMENTO "

```html
<!DOCTYPE html>
<html lang="pt-BR">
<head>
<meta charset="UTF-8">
<title>Andaimes para obras de todos os tamanhos</title>
<link href="https://fonts.googleapis.com/css2?family=Montserrat:wght@300;400;600;800&display=swap" rel="stylesheet">
<style>
  :root {
    --charcoal-dark: #1b1b1c;
    --charcoal: #2c2c2e;
    --yellow: #f4b62c;
    --yellow-light: #f8c94a;
    --white: #ffffff;
    --steel-light: #d9dcdf;
    --steel: #9ea3a8;
  }
  * { margin: 0; padding: 0; box-sizing: border-box; }
  html, body { width: 1200px; height: 1200px; overflow: hidden; }
  body { font-family: "Montserrat", sans-serif; background: var(--charcoal-dark); }
  .post {
    position: relative;
    width: 1200px;
    height: 1200px;
    overflow: hidden;
    background: linear-gradient(135deg, var(--charcoal) 0%, var(--charcoal-dark) 100%);
  }
  .yellow-field {
    position: absolute;
    left: 560px;
    top: 0;
    width: 640px;
    height: 820px;
    background: linear-gradient(160deg, var(--yellow-light), var(--yellow));
    border-bottom-left-radius: 420px;
  }
  .social-handle {
    position: absolute;
    top: 30px;
    right: 24px;
    display: flex;
    align-items: center;
    gap: 12px;
    color: var(--white);
    font-size: 25px;
    font-weight: 600;
    letter-spacing: 1.5px;
  }
  .social-handle .marker { width: 24px; height: 24px; background: var(--white); border-radius: 4px; }
  .scaffold-art {
    position: absolute;
    left: 650px;
    top: 215px;
    width: 550px;
    height: 820px;
    background: linear-gradient(180deg, var(--steel-light) 0%, var(--steel) 100%);
    opacity: 0.85;
  }
  .headline { position: absolute; left: 84px; top: 396px; color: var(--white); }
  .headline .tag {
    display: inline-block;
    background: var(--yellow);
    color: var(--charcoal-dark);
    font-weight: 800;
    font-size: 74px;
    line-height: 1;
    padding: 8px 22px 10px;
    border-radius: 18px;
    margin-bottom: 18px;
  }
  .headline .line {
    display: block;
    font-weight: 300;
    font-size: 74px;
    line-height: 1.12;
    text-align: center;
    width: 432px;
  }
  .headline .line.strong { font-weight: 800; }
  .brand { position: absolute; left: 60px; top: 1020px; color: var(--white); }
  .brand .name-row { display: flex; align-items: center; gap: 22px; }
  .brand .mark { width: 92px; height: 92px; background: var(--yellow); }
  .brand .name { font-size: 58px; font-weight: 600; letter-spacing: 2px; line-height: 1; }
  .brand .division { font-size: 22px; font-weight: 600; letter-spacing: 5px; color: var(--white); margin-top: 6px; }
  .brand .partners { margin-top: 22px; font-size: 20px; font-weight: 600; letter-spacing: 1.5px; }
</style>
</head>
<body>
  <main class="post">
    <div class="yellow-field"></div>

    <div class="social-handle">
      <span class="marker"></span>
      <span>@VORTAEQUIPAMENTOS</span>
    </div>

    <div class="scaffold-art" role="img" aria-label="Estrutura de andaime metálico com plataformas, guarda-corpos e escada com gaiola"></div>

    <h1 class="headline">
      <span class="tag">ANDAIMES</span>
      <span class="line">para obras</span>
      <span class="line">de todos os</span>
      <span class="line strong">TAMANHOS!</span>
    </h1>

    <footer class="brand">
      <div class="name-row">
        <span class="mark"></span>
        <div>
          <div class="name">VORTA</div>
          <div class="division">EQUIPAMENTOS</div>
        </div>
      </div>
      <div class="partners">TUBAX ANDAIMES | FERMAQ</div>
    </footer>
  </main>
</body>
</html>
```